IT COMPANYcutting edge tec business card

we are IT company that building any apps.
we need business card in japanese and english
You don’t have to include all information in front one you can attach part of that information to back-side
company name : 株式会社ひかりの丘 (BRIGHTHILL Inc.)
concept : cutting-edge technology
role : 取締役 (director)
name : 呉 炫秀 (Oh Hyeonsuk)
post number : 154-0038
address : 東京都世田谷区西若葉台5-14-8 (5-14-8, Nishiwakabadai, Setagaya Ku, Tokyo To, 154-0038, Japan)
Tel:+81-3-5917-2846
Mobile:+81-80-7253-3169
Email : hoh@brighthill-lab.com
website : www.brighthill-lab.com

we dont have logo so please make it as well
we also looking for designer who can make homapage design.

Contact Information for Business Card

cutting-edge design and modern for IT

Font styles to use
Sans Serif

Colors
34a6d7
33b8a4
6092c4
3377b5
886aae
6b449b
b868aa
a64599

Requirements
Must have
• Simple but designed

```html
<!DOCTYPE html>
<html lang="ja">
<head>
<meta charset="utf-8">
<title>BRIGHTHILL Inc. Business Card</title>
<link href="https://fonts.googleapis.com/css2?family=Lato:wght@400;700&family=Noto+Sans+JP:wght@400;500&display=swap" rel="stylesheet">
<style>
  :root {
    --backdrop: #3d3d3d;
    --card: #ffffff;
    --purple-deep: #6b449b;
    --purple-soft: #886aae;
    --sky: #34a6d7;
    --teal: #33b8a4;
  }
  * { box-sizing: border-box; margin: 0; padding: 0; }
  html, body {
    width: 1200px; height: 750px; overflow: hidden;
    background: var(--backdrop);
    font-family: "Lato", "Noto Sans JP", sans-serif;
  }
  .canvas { position: relative; width: 1200px; height: 750px; }
  .card {
    position: absolute; top: 186px;
    width: 560px; height: 328px;
    background: var(--card);
    border-radius: 18px;
    text-align: center;
  }
  .card--front { left: 38px; }
  .card--back { left: 610px; width: 562px; }
  .brand-mark {
    position: absolute; left: 50%;
    width: 56px; height: 56px; margin-left: -28px;
    border-radius: 50%;
    background: var(--purple-deep);
  }
  .card--front .brand-mark { top: 36px; }
  .card--back .brand-mark { top: 62px; }
  .row { position: absolute; left: 0; right: 0; }
  .company-en {
    top: 124px; font-size: 15.5px; font-weight: 700; color: var(--purple-soft);
  }
  .person-name {
    top: 158px; font-size: 22.5px; font-weight: 700; color: var(--purple-deep);
  }
  .person-role {
    top: 187px; font-size: 14.5px; font-weight: 700; color: var(--sky);
  }
  .contact {
    top: 225px;
    display: grid; grid-template-columns: 1fr auto 1fr;
    column-gap: 14px; row-gap: 4px;
    font-size: 14.5px; font-weight: 700; color: var(--purple-deep);
  }
  .contact .left { text-align: right; }
  .contact .right { text-align: left; }
  .contact .divider { color: var(--sky); font-weight: 400; }
  .company-jp {
    top: 160px;
    font-family: "Noto Sans JP", sans-serif;
    font-size: 26px; font-weight: 400; color: var(--purple-deep);
    letter-spacing: 0.5px;
  }
  .address {
    top: 230px;
    font-size: 15.5px; line-height: 19.5px; color: var(--teal);
  }
  .address .jp { font-family: "Noto Sans JP", "Lato", sans-serif; font-weight: 400; display: block; }
  .address .en { font-weight: 700; display: block; }
  .address .postal { font-weight: 400; display: block; }
</style>
</head>
<body>
<div class="canvas">
  <section class="card card--front">
    <div class="brand-mark"></div>
    <p class="row company-en">BRIGHTHILL Inc.</p>
    <p class="row person-name">Oh Hyeonsuk</p>
    <p class="row person-role">Director</p>
    <div class="row contact">
      <span class="left">+81-3-5917-2846</span>
      <span class="divider">|</span>
      <span class="right">+81-80-7253-3169</span>
      <span class="left">hoh@brighthill-lab.com</span>
      <span class="divider">|</span>
      <span class="right">www.brighthill-lab.com</span>
    </div>
  </section>

  <section class="card card--back">
    <div class="brand-mark"></div>
    <p class="row company-jp">株式会社ひかりの丘</p>
    <p class="row address">
      <span class="jp">東京都世田谷区西若葉台5-14-8</span>
      <span class="en">5-14-8, Nishiwakabadai, Setagaya Ku,<br>Tokyo To, 154-0038, Japan</span>
      <span class="postal">P.O:154-0038</span>
    </p>
  </section>
</div>
</body>
</html>
```